Land Development Company Website Redesign

We are looking for a fresh design for our website. The content will remain 90% the same.

We really like the layout style of www.quibbenstor.com.

We have attached our current site for content.

Industry/Entity Type

Real Estate Development

Coding

Coded - Design and coding required

Number of Pages Required

5+ page

Font styles to use
Sans Serif

Requirements
Must have
• Consistent feel across all the pages. Visually appealing and simple layout design that can be viewed on a mobile device and browser.

```html
<!DOCTYPE html>
<html lang="en">
<head>
<meta charset="utf-8">
<title>Aldermoor Estates</title>
<link href="https://fonts.googleapis.com/css2?family=Roboto:wght@300;400;500;700&family=Open+Sans:ital,wght@0,400;0,600;1,400&display=swap" rel="stylesheet">
<style>
  :root {
    --gold: #c9a447;
    --gold-soft: #f4e6b8;
    --ink: #2b2b2b;
    --text: #555555;
    --muted: #8a8a8a;
    --line: #e3e3e3;
    --panel: #f2f2f2;
    --footer: #262626;
    --white: #ffffff;
  }
  * { box-sizing: border-box; margin: 0; padding: 0; }
  html, body { width: 795px; height: 1200px; overflow: hidden; background: var(--white); }
  body { font-family: "Open Sans", Arial, sans-serif; color: var(--text); }
  .page { position: relative; width: 795px; height: 1200px; overflow: hidden; }

  /* Header */
  .site-header { height: 38px; display: flex; align-items: center; justify-content: space-between; padding: 0 52px 0 50px; background: var(--white); position: relative; z-index: 2; }
  .brand { display: flex; align-items: center; gap: 8px; }
  .brand-mark { width: 22px; height: 28px; background: var(--ink); }
  .brand-name { font-family: "Roboto", Arial, sans-serif; font-size: 9px; font-weight: 500; color: var(--ink); letter-spacing: .5px; text-transform: uppercase; }
  .main-nav { display: flex; gap: 20px; }
  .main-nav a { font-family: "Roboto", Arial, sans-serif; font-size: 8.5px; color: var(--ink); text-decoration: none; letter-spacing: .4px; font-weight: 500; }

  /* Hero */
  .hero { position: relative; height: 322px; background: linear-gradient(180deg, #6f93bd 0%, #a9c2dc 35%, #dfe6ea 55%, #8da06a 72%, #3f5a2c 100%); }
  .hero-dots { position: absolute; right: 14px; top: 140px; display: flex; flex-direction: column; gap: 6px; }
  .hero-dots span { width: 6px; height: 6px; border-radius: 50%; background: rgba(255,255,255,.6); }
  .hero-dots span.is-active { background: var(--white); }

  /* Welcome */
  .welcome { position: relative; text-align: center; padding: 26px 70px 22px; background: radial-gradient(ellipse 60% 80% at 50% 0%, var(--gold-soft) 0%, rgba(244,230,184,0) 70%); }
  .welcome-kicker { font-family: "Roboto", Arial, sans-serif; font-size: 15px; font-weight: 500; color: var(--ink); letter-spacing: 1px; }
  .welcome-title { font-family: "Roboto", Arial, sans-serif; font-size: 19px; font-weight: 500; color: var(--gold); letter-spacing: 1px; margin-top: 2px; }
  .welcome-text { font-size: 9px; line-height: 1.6; margin: 12px auto 0; max-width: 650px; }
  .learn-more { display: inline-block; margin-top: 12px; font-family: "Roboto", Arial, sans-serif; font-size: 8px; color: var(--gold); text-decoration: none; letter-spacing: .8px; font-weight: 500; }
  .divider { width: 80px; height: 1px; background: var(--gold); margin: 6px auto 0; }

  /* Homes */
  .homes { padding: 14px 53px 0; text-align: center; }
  .section-title { font-family: "Roboto", Arial, sans-serif; font-size: 19px; font-weight: 500; color: var(--ink); letter-spacing: 1px; }
  .section-title em { font-style: normal; color: var(--gold); }
  .home-list { display: flex; gap: 20px; margin-top: 14px; text-align: left; }
  .home-card { width: 216px; border: 1px solid var(--line); background: var(--white); }
  .home-photo { height: 128px; }
  .home-photo.one { background: linear-gradient(180deg, #7fa4c6 0%, #b9c9a3 45%, #6f8a47 100%); }
  .home-photo.two { background: linear-gradient(180deg, #8aa9cc 0%, #d8d0c0 50%, #7a8f5a 100%); }
  .home-photo.three { background: linear-gradient(180deg, #a9c3dc 0%, #b88a6c 50%, #6e8248 100%); }
  .home-body { padding: 9px 10px 10px; }
  .home-features { font-size: 7.5px; line-height: 1.55; color: var(--text); }
  .home-meta { display: flex; justify-content: space-between; align-items: flex-end; margin-top: 8px; }
  .home-size { font-family: "Roboto", Arial, sans-serif; font-size: 9px; font-weight: 500; color: var(--ink); }
  .home-price { font-family: "Roboto", Arial, sans-serif; font-size: 12px; font-weight: 500; color: var(--gold); margin-top: 3px; }
  .btn-detail { display: inline-flex; align-items: center; gap: 4px; border: 1px solid var(--gold); color: var(--gold); font-family: "Roboto", Arial, sans-serif; font-size: 7px; font-weight: 500; padding: 4px 10px; text-decoration: none; letter-spacing: .4px; margin-bottom: 14px; }
  .btn-more { display: inline-block; margin-top: 22px; border: 1px solid var(--gold); color: var(--gold); font-family: "Roboto", Arial, sans-serif; font-size: 8px; font-weight: 500; padding: 6px 18px; text-decoration: none; letter-spacing: .6px; }

  /* Testimonials */
  .testimonials { position: absolute; top: 915px; left: 0; width: 795px; height: 205px; background: var(--panel); padding: 22px 60px 0; text-align: center; }
  .quote-list { display: flex; gap: 40px; margin-top: 20px; text-align: left; }
  .quote { flex: 1; display: flex; gap: 14px; }
  .avatar { width: 52px; height: 52px; border-radius: 50%; flex: none; background: radial-gradient(circle at 50% 40%, #d9bfa6 0%, #8a7a6e 70%); }
  .quote-text { font-size: 8px; font-style: italic; line-height: 1.6; color: var(--muted); position: relative; padding-left: 12px; }
  .quote-text::before { content: "\201C"; position: absolute; left: 0; top: -6px; font-size: 20px; color: var(--gold); font-style: normal; }
  .quote-author { font-family: "Roboto", Arial, sans-serif; font-size: 9px; font-weight: 500; color: var(--gold); margin-top: 8px; padding-left: 12px; }
  .quote-role { font-size: 7.5px; color: var(--muted); padding-left: 12px; }
  .quote-dots { display: flex; justify-content: center; gap: 5px; margin-top: 20px; }
  .quote-dots span { width: 5px; height: 5px; border-radius: 50%; background: #c8c8c8; }
  .quote-dots span.is-active { background: var(--gold); }

  /* Footer */
  .site-footer { position: absolute; bottom: 0; left: 0; width: 795px; height: 80px; background: var(--footer); padding: 22px 53px 0; display: flex; justify-content: space-between; }
  .footer-nav { display: flex; gap: 8px; }
  .footer-nav a, .footer-nav span { font-family: "Roboto", Arial, sans-serif; font-size: 8px; color: var(--white); text-decoration: none; letter-spacing: .4px; }
  .copyright { font-size: 7px; color: var(--muted); margin-top: 12px; }
  .social { display: flex; gap: 6px; }
  .social span { width: 20px; height: 20px; border-radius: 50%; background: var(--gold); }
</style>
</head>
<body>
<div class="page">
  <header class="site-header">
    <div class="brand"><span class="brand-mark"></span><span class="brand-name">Aldermoor Estates</span></div>
    <nav class="main-nav">
      <a href="#">WHAT'S NEW</a><a href="#">THE ESTATES</a><a href="#">THE TEAM</a><a href="#">GALLERY</a><a href="#">CONTACT</a>
    </nav>
  </header>

  <section class="hero" role="img" aria-label="Photograph of a hilltop castle estate among green trees under a blue sky">
    <div class="hero-dots"><span class="is-active"></span><span></span><span></span></div>
  </section>

  <section class="welcome">
    <h2 class="welcome-kicker">WELCOME TO</h2>
    <h1 class="welcome-title">ALDERMOOR ESTATES</h1>
    <p class="welcome-text">A big part of the Aldermoor Estates vision is that the homes here are architecturally pleasing and fit with the overall design of Aldermoor Estates and the Ridgeline Specific Plan. For this reason, an architectural review committee will review all plans to make sure builders adhere to published design standards. Here are some available homes currently listed in the community.</p>
    <a class="learn-more" href="#">LEARN MORE</a>
    <div class="divider"></div>
  </section>

  <section class="homes">
    <h2 class="section-title">AVAILABLE <em>HOMES</em></h2>
    <div class="home-list">
      <article class="home-card">
        <div class="home-photo one" role="img" aria-label="Photograph of a two-storey stucco home with a tiled roof"></div>
        <div class="home-body">
          <p class="home-features">5 Bdrms, 4.5 Baths, Casita (Guest Studio), Huge Gymnasium, Covered Patio, Courtyard with dramatic 18' Ceiling</p>
          <div class="home-meta">
            <div><div class="home-size">3890 sq ft</div><div class="home-price">$1,000,000</div></div>
            <a class="btn-detail" href="#">&#8250; GET DETAIL</a>
          </div>
        </div>
      </article>
      <article class="home-card">
        <div class="home-photo two" role="img" aria-label="Photograph of a large stone-front family home"></div>
        <div class="home-body">
          <p class="home-features">5 Bdrms, 4.5 Baths, Casita (Guest Studio), Huge Gymnasium, Covered Patio, Courtyard with dramatic 18' Ceiling</p>
          <div class="home-meta">
            <div><div class="home-size">3890 sq ft</div><div class="home-price">$1,000,000</div></div>
            <a class="btn-detail" href="#">&#8250; GET DETAIL</a>
          </div>
        </div>
      </article>
      <article class="home-card">
        <div class="home-photo three" role="img" aria-label="Photograph of a brick home with a manicured front lawn"></div>
        <div class="home-body">
          <p class="home-features">5 Bdrms, 4.5 Baths, Casita (Guest Studio), Huge Gymnasium, Covered Patio, Courtyard with dramatic 18' Ceiling</p>
          <div class="home-meta">
            <div><div class="home-size">3890 sq ft</div><div class="home-price">$1,000,000</div></div>
            <a class="btn-detail" href="#">&#8250; GET DETAIL</a>
          </div>
        </div>
      </article>
    </div>
    <a class="btn-more" href="#">CLICK HERE TO VIEW MORE</a>
  </section>

  <section class="testimonials">
    <h2 class="section-title">WHAT OUR <em>CLIENT SAY'S</em></h2>
    <div class="quote-list">
      <div class="quote">
        <div class="avatar" role="img" aria-label="Client portrait"></div>
        <div>
          <p class="quote-text">Lorem ipsum dolor sit amet, consectetur adipiscing elit sed do eiusmod tempor incididunt ut labore et dolore magna aliqua. Lorem ipsum dolor amet consectetur.</p>
          <div class="quote-author">By Author Name</div>
          <div class="quote-role">CEO, Location</div>
        </div>
      </div>
      <div class="quote">
        <div class="avatar" role="img" aria-label="Client portrait"></div>
        <div>
          <p class="quote-text">Lorem ipsum dolor sit amet, consectetur adipiscing elit sed do eiusmod tempor incididunt ut labore et dolore magna aliqua. Lorem ipsum dolor amet consectetur.</p>
          <div class="quote-author">By Author Name</div>
          <div class="quote-role">CEO, Location</div>
        </div>
      </div>
    </div>
    <div class="quote-dots"><span class="is-active"></span><span></span></div>
  </section>

  <footer class="site-footer">
    <div>
      <nav class="footer-nav">
        <a href="#">HOME</a><span>|</span><a href="#">WHAT'S NEW</a><span>|</span><a href="#">THE ESTATES</a><span>|</span><a href="#">THE TEAM</a><span>|</span><a href="#">GALLERY</a><span>|</span><a href="#">CONTACT</a>
      </nav>
      <p class="copyright">Copyright (c) 2015, Aldermoor Estates, All Rights Reserved</p>
    </div>
    <div class="social"><span></span><span></span><span></span></div>
  </footer>
</div>
</body>
</html>
```